Megafield Party Poster 50 2016

We are looking for a designer to create A0 A3 and A4 versions of a Megafield Party Poster. The poster is for a special event we are having at the restaurant for the big game!

We have included in the brief some examples of other posters that other locations have made for both the current game and past games.

• The poster must have on it somewhere the following:
• MEGA FIELD 50
• Free Entry
• Monday, February 8th, 2016 OPEN at 9am
• 25 HD Screens
• Prize Giveaways / Breakfast Burger and Beer Breakfast Pregame / Wings, Pizzas, Beer Towers, Buckets,
• KTO940 Radio Live Crossover Onsite
• RESERVE YOUR TABLE NOW
• 1 3000 FEAST

```html
<!DOCTYPE html>
<html lang="en">
<head>
<meta charset="utf-8">
<title>Megafield 50 Party Poster</title>
<link rel="stylesheet" href="https://fonts.googleapis.com/css2?family=Anton&family=Bebas+Neue&display=swap">
<style>
  :root {
    --white: #ffffff;
    --ink: #1c1a17;
    --olive-dark: #3f4a14;
    --olive-light: #a7b64a;
    --sky-violet: #b9a6d8;
    --sky-blue: #3b78c9;
    --night: #0d1b3a;
    --turf: #6f8c2c;
    --turf-light: #b7c86a;
    --shadow: rgba(0, 0, 0, 0.35);
  }
  * { margin: 0; padding: 0; box-sizing: border-box; }
  html, body { width: 848px; height: 1200px; overflow: hidden; background: var(--night); }
  .poster {
    position: relative;
    width: 848px;
    height: 1200px;
    overflow: hidden;
    font-family: "Bebas Neue", "Anton", sans-serif;
    color: var(--white);
  }
  .stadium-backdrop {
    position: absolute; inset: 0;
    background:
      radial-gradient(ellipse 60% 30% at 75% 28%, rgba(120,180,255,0.55), transparent 70%),
      radial-gradient(ellipse 45% 30% at 10% 35%, rgba(220,210,255,0.8), transparent 70%),
      radial-gradient(ellipse 40% 20% at 5% 58%, rgba(220,90,160,0.45), transparent 70%),
      linear-gradient(180deg, #27345c 0%, #6b6fa8 18%, #9fb3e0 33%, #3e5b86 48%, #2b2f2c 60%, #4c5a2a 78%, var(--turf) 88%, var(--turf-light) 100%);
  }
  .headline {
    position: absolute; left: 60px; top: 20px; width: 740px; height: 230px;
    font-family: "Anton", sans-serif;
  }
  .headline text { fill: var(--white); font-size: 122px; letter-spacing: 1px; }
  .edition-number {
    position: absolute; left: 240px; top: 100px; width: 400px;
    font-family: "Anton", sans-serif; font-size: 455px; line-height: 1;
    text-align: center; letter-spacing: -6px;
    text-shadow: 0 6px 18px var(--shadow);
  }
  .edition-year {
    position: absolute; left: 362px; top: 370px;
    font-family: "Anton", sans-serif; font-size: 82px; line-height: 1;
    text-shadow: 0 3px 8px var(--shadow);
  }
  .event-date { position: absolute; left: 43px; top: 308px; text-align: left; text-shadow: 0 2px 6px var(--shadow); }
  .event-date .day { font-size: 22px; line-height: 1; }
  .event-date .opening { font-size: 38px; line-height: 1; }
  .matchup {
    position: absolute; left: 662px; top: 292px; width: 156px; text-align: center;
    text-shadow: 0 2px 6px var(--shadow); line-height: 0.9;
  }
  .matchup .team { font-size: 40px; display: block; }
  .matchup .versus { font-size: 22px; font-style: italic; display: block; margin: -2px 0; }
  .venue-badge {
    position: absolute; left: 37px; top: 520px; width: 222px; height: 222px; border-radius: 50%;
    background: var(--white); color: var(--ink);
    display: flex; align-items: center; justify-content: center; text-align: center;
    font-size: 34px; line-height: 1; padding: 30px;
  }
  .features { position: absolute; left: 0; top: 0; }
  .feature-band {
    position: absolute; left: -10px; width: 418px; height: 64px;
    background: var(--white); color: var(--ink);
    transform: rotate(-6deg); transform-origin: left center;
    display: flex; align-items: center; justify-content: center;
    font-size: 44px; line-height: 1; box-shadow: 0 3px 10px var(--shadow);
  }
  .feature-band.giveaways { top: 732px; }
  .feature-band.screens { top: 812px; }
  .feature-band.radio { top: 892px; font-size: 36px; }
  .pregame { position: absolute; left: 502px; top: 556px; width: 308px; text-align: center; text-shadow: 0 2px 6px var(--shadow); }
  .pregame-title { width: 308px; height: 50px; display: block; font-family: "Anton", sans-serif; }
  .pregame-title text { fill: var(--white); font-size: 36px; }
  .pregame .pairing { font-size: 30px; line-height: 1; margin-top: -2px; }
  .pregame .label { display: flex; align-items: center; gap: 10px; font-size: 30px; line-height: 1; margin-top: 6px; }
  .pregame .label::before, .pregame .label::after { content: ""; flex: 1; height: 1px; background: var(--white); }
  .menu-card { position: absolute; left: 502px; top: 685px; width: 308px; height: 280px; }
  .menu-list {
    position: absolute; left: 45px; top: 14px; width: 218px; list-style: none;
    text-align: center; color: var(--ink);
  }
  .menu-list li { font-size: 42px; line-height: 1; padding: 6px 0 5px; border-bottom: 1px solid var(--ink); }
  .menu-list li:last-child { border-bottom: none; color: #4a4630; }
  .entry-banner { position: absolute; left: 218px; top: 993px; width: 437px; height: 96px; }
  .entry-banner .title {
    position: absolute; inset: 0; display: flex; align-items: center; justify-content: center;
    font-family: "Anton", sans-serif; font-size: 78px; line-height: 1; letter-spacing: -1px;
    background: linear-gradient(180deg, var(--olive-dark), var(--olive-light) 60%, var(--olive-dark));
    -webkit-background-clip: text; background-clip: text; color: transparent;
  }
  .booking { position: absolute; left: 218px; top: 1084px; width: 437px; text-align: center; text-shadow: 0 2px 6px var(--shadow); }
  .booking .prompt { font-size: 36px; line-height: 1; }
  .booking .phone { font-family: "Anton", sans-serif; font-size: 54px; line-height: 1.05; }
</style>
</head>
<body>
<main class="poster">
  <div class="stadium-backdrop" role="img" aria-label="Blurred floodlit football stadium with a green field at night"></div>

  <svg class="headline" viewBox="0 0 740 230" aria-label="Megafield">
    <defs><path id="headline-arc" d="M20 215 Q370 40 720 215"/></defs>
    <text text-anchor="middle"><textPath href="#headline-arc" startOffset="50%">MEGAFIELD</textPath></text>
  </svg>

  <div class="edition-number">50</div>
  <div class="edition-year">2016</div>

  <div class="event-date">
    <p class="day">MON. 8TH FEBRUARY</p>
    <p class="opening">OPEN AT 9AM</p>
  </div>

  <div class="matchup">
    <span class="team">HARBORMEN</span>
    <span class="versus">vs</span>
    <span class="team">REDWINGS</span>
  </div>

  <div class="venue-badge">THE OVEN &amp; EMBER CO.</div>

  <div class="features">
    <div class="feature-band giveaways">PRIZE GIVEAWAYS</div>
    <div class="feature-band screens">25 HD SCREENS</div>
    <div class="feature-band radio">KTO940 RADIO CROSSOVER LIVE</div>
  </div>

  <div class="pregame">
    <svg class="pregame-title" viewBox="0 0 308 50" aria-label="Breakfast Burger">
      <defs><path id="pregame-arc" d="M4 46 Q154 14 304 46"/></defs>
      <text text-anchor="middle"><textPath href="#pregame-arc" startOffset="50%">BREAKFAST BURGER</textPath></text>
    </svg>
    <p class="pairing">&amp; BREAKFAST BEER</p>
    <p class="label">PREGAME</p>
  </div>

  <div class="menu-card">
    <svg width="308" height="280" viewBox="0 0 308 280" aria-hidden="true">
      <path d="M0 0 H308 V280 L154 245 L0 280 Z" fill="var(--white)"/>
    </svg>
    <ul class="menu-list">
      <li>WINGS</li>
      <li>PIZZAS</li>
      <li>BEER TOWERS</li>
      <li>BUCKETS</li>
    </ul>
  </div>

  <div class="entry-banner">
    <svg width="437" height="96" viewBox="0 0 437 96" aria-hidden="true">
      <path d="M0 0 H437 L405 48 L437 96 H0 L32 48 Z" fill="var(--white)"/>
    </svg>
    <p class="title">FREE ENTRY</p>
  </div>

  <div class="booking">
    <p class="prompt">RESERVE YOUR TABLE NOW</p>
    <p class="phone">CALL 13000-FEAST</p>
  </div>
</main>
</body>
</html>
```